Accounting firm needing business card / letterhead designed
Marcus T. Elbering, CPA
marcus@fernquill.com
www.fernquill.com
482 N Harlow Ave Halvern, MN 55719
612-555-0172

```html
<!DOCTYPE html>
<html lang="en">
<head>
<meta charset="utf-8">
<title>Fernquill Practice Solutions – Business Card</title>
<link href="https://fonts.googleapis.com/css2?family=Open+Sans:wght@400;600;700&display=swap" rel="stylesheet">
<style>
  :root {
    --navy: #251f5f;
    --green: #8cc63f;
    --white: #ffffff;
    --backdrop: #ececec;
    --card-w: 340px;
    --card-h: 586px;
  }
  * { box-sizing: border-box; margin: 0; padding: 0; }
  html, body {
    width: 1200px;
    height: 786px;
    overflow: hidden;
    background: var(--backdrop);
    font-family: "Open Sans", Arial, sans-serif;
  }
  .canvas {
    position: relative;
    width: 1200px;
    height: 786px;
  }
  .card {
    position: absolute;
    top: 100px;
    width: var(--card-w);
    height: var(--card-h);
  }
  .card--front {
    left: 220px;
    background: var(--white);
    color: var(--navy);
    text-align: center;
  }
  .card--back {
    left: 640px;
    background: var(--navy);
  }

  /* Front */
  .wordmark {
    position: absolute;
    top: 72px;
    left: 0;
    right: 0;
    color: var(--navy);
  }
  .wordmark__name {
    font-weight: 700;
    font-size: 40px;
    letter-spacing: 1px;
    line-height: 1;
    text-transform: uppercase;
  }
  .wordmark__line {
    margin-top: 6px;
    font-weight: 700;
    font-size: 11px;
    letter-spacing: 3px;
    text-transform: uppercase;
  }
  .address {
    position: absolute;
    top: 150px;
    left: 0;
    right: 0;
    font-size: 14px;
    line-height: 19px;
  }
  .person {
    position: absolute;
    top: 292px;
    left: 50%;
    transform: translateX(-50%);
    width: 196px;
  }
  .person__name {
    font-size: 18px;
    line-height: 24px;
    white-space: nowrap;
  }
  .person__rule {
    display: block;
    height: 4px;
    margin-top: 6px;
    background: var(--green);
  }
  .contact {
    position: absolute;
    top: 378px;
    left: 0;
    right: 0;
    font-size: 14px;
    line-height: 19px;
  }
  .web-band {
    position: absolute;
    bottom: 0;
    left: 62px;
    width: 210px;
    height: 50px;
    background: var(--navy);
    color: var(--white);
    font-size: 13px;
    letter-spacing: 1.5px;
    line-height: 50px;
  }

  /* Back */
  .card--back .wordmark {
    top: 218px;
    left: 24px;
    right: 20px;
    color: var(--white);
    display: flex;
    align-items: center;
    gap: 10px;
  }
  .card--back .wordmark__name { font-size: 40px; }
  .card--back .wordmark__line { font-size: 11px; letter-spacing: 4px; }
  .brand-square {
    flex: none;
    width: 18px;
    height: 18px;
    background: var(--green);
  }
</style>
</head>
<body>
<main class="canvas">
  <section class="card card--front" aria-label="Business card front">
    <div class="wordmark">
      <p class="wordmark__name">Fernquill</p>
      <p class="wordmark__line">Practice Solutions</p>
    </div>
    <p class="address">482 N Harlow Ave<br>Halvern, MN 55719</p>
    <div class="person">
      <p class="person__name">Marcus T. Elbering, CPA</p>
      <span class="person__rule"></span>
    </div>
    <p class="contact">612-555-0172<br>marcus@fernquill.com</p>
    <p class="web-band">www.fernquill.com</p>
  </section>

  <section class="card card--back" aria-label="Business card back">
    <div class="wordmark">
      <span class="brand-square"></span>
      <div>
        <p class="wordmark__name">Fernquill</p>
        <p class="wordmark__line">Practice Solutions</p>
      </div>
    </div>
  </section>
</main>
</body>
</html>
```